Vietnamese Restaurant Poster

We are a family restaurant specializing in Vietnamese comfort food of pho (Vietnamese Beef Noodle Soup).

We need to create a poster that will attract customers driving by our restaurant.

This poster will be placed on sandwich boards and placed on the intersecting streets.

We want it to be
- big and visually appealing.
- Preferably with a logo incorporating our name and a bowl of Pho
- a arrow sign pointing right
- our phone number 604-318-7915

The name of our restaurant is:

Pho Lanh Tuyet (Title text)
Vietnamese Restaurant (smaller text)

Reason: We have narrowed it down to 2  designs that we absolutely love. Thank you to all who have submitted.

Target Market(s)

Caucasian people who have not tried Vietnamese food. Our location is a little hidden so we want to make these posters to put on the main streets which will grab attention of people driving by to come into our restaurant

Industry/Entity Type

Restaurant

Requirements
Must have
• - big and visually appealing.
logo incorporating our name and a bowl of Pho
Nice to have
• a person eating a bowl of pho

```html
<!DOCTYPE html>
<html lang="en">
<head>
<meta charset="utf-8">
<title>Pho Lanh Tuyet – Vietnamese Restaurant</title>
<link rel="stylesheet" href="https://fonts.googleapis.com/css2?family=Abril+Fatface&family=Playfair+Display:wght@700;900&display=swap">
<style>
  :root {
    --sky-light: #e4f4fb;
    --sky-mid: #bfe3f4;
    --sky-deep: #9dd3ee;
    --wine: #8a1a2b;
    --wine-dark: #7a1020;
    --ray: rgba(255,255,255,0.45);
    --mascot-light: #f4f1ee;
    --mascot-dark: #2a2a2a;
  }
  * { margin: 0; padding: 0; box-sizing: border-box; }
  html, body { width: 1200px; height: 900px; overflow: hidden; }
  .poster {
    position: relative;
    width: 1200px;
    height: 900px;
    overflow: hidden;
    background: linear-gradient(160deg, var(--sky-deep) 0%, var(--sky-mid) 45%, var(--sky-light) 100%);
  }
  .rays, .arrow-band { position: absolute; left: 0; top: 0; }
  .mascot {
    position: absolute;
    left: 18px;
    top: 50px;
    width: 430px;
    height: 650px;
    border-radius: 46% 46% 30% 30% / 30% 30% 18% 18%;
    background: radial-gradient(ellipse at 50% 40%, var(--mascot-light) 0%, #e3e0dc 55%, #9b9896 85%, var(--mascot-dark) 100%);
  }
  .brand {
    position: absolute;
    left: 400px;
    top: 270px;
    width: 780px;
    text-align: center;
    color: var(--wine);
  }
  .brand-name {
    font-family: "Abril Fatface", "Playfair Display", serif;
    font-weight: 400;
    font-size: 96px;
    line-height: 1;
    letter-spacing: 1px;
    transform: scaleX(0.86);
    white-space: nowrap;
  }
  .brand-tagline {
    margin-top: 34px;
    font-family: "Playfair Display", serif;
    font-weight: 900;
    font-size: 44px;
    line-height: 1;
  }
  .contact {
    position: absolute;
    left: 578px;
    top: 508px;
    display: flex;
    align-items: center;
    gap: 16px;
    color: var(--wine);
  }
  .contact-icon {
    width: 58px;
    height: 58px;
    border-radius: 8px;
    background: var(--wine);
    display: flex;
    align-items: center;
    justify-content: center;
  }
  .contact-number {
    font-family: "Playfair Display", serif;
    font-weight: 900;
    font-size: 31px;
    letter-spacing: 1px;
  }
</style>
</head>
<body>
<main class="poster">
  <svg class="rays" width="1200" height="900" viewBox="0 0 1200 900" aria-hidden="true">
    <polygon points="0,900 0,0 40,0" fill="var(--ray)"/>
    <polygon points="0,900 120,0 200,0" fill="var(--ray)" opacity="0.7"/>
    <polygon points="0,900 480,0 560,0" fill="var(--ray)" opacity="0.5"/>
    <polygon points="0,900 760,120 800,160" fill="var(--ray)" opacity="0.6"/>
    <polygon points="0,900 1200,300 1200,360" fill="var(--ray)" opacity="0.4"/>
    <polygon points="0,900 1200,600 1200,640" fill="var(--ray)" opacity="0.5"/>
  </svg>

  <svg class="arrow-band" width="1200" height="900" viewBox="0 0 1200 900" aria-hidden="true">
    <g fill="var(--wine-dark)">
      <polygon points="-345,670 -215,670 -135,765 -215,860 -345,860 -265,765" opacity="0.12"/>
      <polygon points="-215,670 -85,670 -5,765 -85,860 -215,860 -135,765" opacity="0.18"/>
      <polygon points="-85,670 45,670 125,765 45,860 -85,860 -5,765" opacity="0.24"/>
      <polygon points="45,670 175,670 255,765 175,860 45,860 125,765" opacity="0.32"/>
      <polygon points="175,670 305,670 385,765 305,860 175,860 255,765" opacity="0.42"/>
      <polygon points="305,670 435,670 515,765 435,860 305,860 385,765" opacity="0.52"/>
      <polygon points="435,670 565,670 645,765 565,860 435,860 515,765" opacity="0.62"/>
      <polygon points="565,670 695,670 775,765 695,860 565,860 645,765" opacity="0.72"/>
      <polygon points="695,670 825,670 905,765 825,860 695,860 775,765" opacity="0.82"/>
      <polygon points="825,670 955,670 1035,765 955,860 825,860 905,765" opacity="0.9"/>
      <polygon points="955,670 1085,670 1165,765 1085,860 955,860 1035,765" opacity="1"/>
    </g>
  </svg>

  <div class="mascot" role="img" aria-label="Cartoon cow chef in a white hat and red scarf holding a tray with a steaming bowl of pho"></div>

  <header class="brand">
    <h1 class="brand-name">Pho Lanh Tuyet</h1>
    <p class="brand-tagline">Vietnamese Restaurant</p>
  </header>

  <div class="contact">
    <span class="contact-icon">
      <svg width="34" height="34" viewBox="0 0 24 24" aria-hidden="true">
        <path fill="#fff" d="M6.6 10.8a15.1 15.1 0 0 0 6.6 6.6l2.2-2.2a1 1 0 0 1 1-.25 11.4 11.4 0 0 0 3.6.57 1 1 0 0 1 1 1V20a1 1 0 0 1-1 1A17 17 0 0 1 3 4a1 1 0 0 1 1-1h3.5a1 1 0 0 1 1 1c0 1.25.2 2.45.57 3.57a1 1 0 0 1-.25 1z"/>
      </svg>
    </span>
    <span class="contact-number">604-318-7915</span>
  </div>
</main>
</body>
</html>
```